New website for Pilates Studio

I need a new version of my website
http://brightcoreflow.biz/
I want an updated fresh look with an easier to read schedule that looks good on mobile phones as well as laptops.
Clean, simple, fresh and BOLD

Target Market(s)

All ages, genders and races

Coding

Number of Pages Required

Colors
9bcb3c

Requirements
Must have
• Photos that mostly use the real images from our studio. Browse our facebook page, website or ask me for high quality images

```html
<!DOCTYPE html>
<html lang="en">
<head>
<meta charset="utf-8">
<title>Bright Core Flow – Pilates Studio</title>
<link href="https://fonts.googleapis.com/css2?family=Arvo:wght@400;700&family=Open+Sans:ital,wght@0,400;0,600;1,400&display=swap" rel="stylesheet">
<style>
:root{
  --gold:#b8962e;
  --gold-light:#cfae4a;
  --olive:#6f8a1e;
  --green:#7fa32a;
  --rust:#b8612a;
  --ink:#333;
  --text:#555;
  --muted:#888;
  --panel:#f0f0f0;
  --footer:#2c2a2b;
  --white:#fff;
}
*{box-sizing:border-box;margin:0;padding:0}
html,body{width:864px;height:1200px;overflow:hidden;background:var(--white)}
body{position:relative;font-family:"Open Sans",Arial,sans-serif;color:var(--text)}
.abs{position:absolute}
.slab{font-family:"Arvo",Georgia,serif}

/* header */
.site-header{left:0;top:0;width:864px;height:78px;background:var(--white);box-shadow:0 1px 3px rgba(0,0,0,.18);z-index:2}
.brand{left:54px;top:20px;display:flex;align-items:center;gap:7px}
.brand-dot{width:22px;height:22px;border-radius:50%;background:var(--gold)}
.brand-name{font-family:"Arvo",Georgia,serif;font-size:18px;color:var(--olive)}
.search{left:685px;top:13px;width:125px;height:20px;background:#efefef}
.search svg{position:absolute;right:6px;top:5px}
.main-nav{left:476px;top:48px;display:flex;font-size:8px;color:var(--ink);letter-spacing:.2px}
.main-nav a{color:inherit;text-decoration:none;padding:7px 14px 0;height:22px;display:block}
.main-nav a.active{color:var(--gold);border-top:2px solid var(--gold);padding-top:5px}

/* hero */
.hero{left:0;top:78px;width:864px;height:322px}
.hero-photo{position:absolute;inset:0;background:linear-gradient(90deg,#b7b9bb 0%,#d9dadb 30%,#c9c9c8 55%,#bdbdbc 100%)}
.hero-title{left:380px;top:102px;width:420px;text-align:center;font-size:26px;color:#3a3a3a}
.hero-copy{left:420px;top:143px;width:340px;text-align:center;font-size:9.2px;line-height:17.5px;color:#444}
.btn{display:block;background:linear-gradient(#cfae4a,#b38f2a);color:var(--white);font-family:"Arvo",Georgia,serif;font-size:10px;text-align:center;text-decoration:none}
.hero-btn{left:548px;top:207px;width:88px;height:23px;line-height:23px}
.arrow{width:44px;height:44px;border-radius:50%;background:rgba(110,110,110,.75);top:131px}
.arrow svg{position:absolute;left:15px;top:14px}

/* welcome */
.welcome-title{left:55px;top:444px;font-size:19px;color:var(--ink)}
.welcome-avatar{left:54px;top:479px;width:109px;height:109px;border-radius:50%;background:linear-gradient(135deg,#8d8a86,#e3e1dd);border:3px solid #fff;box-shadow:0 2px 5px rgba(0,0,0,.35)}
.welcome-sub{left:183px;top:478px;font-size:12px;color:var(--olive)}
.welcome-copy{left:183px;top:505px;width:432px;font-size:8.4px;line-height:18px;color:var(--text)}
.welcome-copy p+p{margin-top:18px}
.welcome-btn{left:183px;top:642px;width:94px;height:27px;line-height:27px;font-size:11px}
.door-photo{left:643px;top:448px;width:167px;height:221px;background:linear-gradient(160deg,#3d4a38 0%,#8a8076 40%,#7a2a2a 60%,#4a4442 100%)}

/* testimonials */
.testimonials{left:0;top:702px;width:864px;height:244px;background:var(--panel)}
.testimonials h2{position:absolute;top:30px;width:864px;text-align:center;font-size:18px;font-weight:400;color:var(--ink)}
.quote-card{top:67px;width:348px;height:75px;background:var(--white);box-shadow:0 0 3px rgba(0,0,0,.08)}
.quote-card::after{content:"";position:absolute;left:30px;bottom:-9px;border:9px solid transparent;border-bottom:0;border-top-color:var(--white)}
.quote-mark{position:absolute;left:14px;top:17px;width:23px;height:23px;background:var(--green)}
.quote-mark svg{position:absolute;left:5px;top:6px}
.quote-text{position:absolute;left:48px;top:13px;width:287px;font-size:8.2px;line-height:16px;color:var(--text);text-align:justify}
.person{top:162px;display:flex;gap:13px;align-items:flex-start}
.person-avatar{width:48px;height:48px;border-radius:50%;background:linear-gradient(135deg,#6a6560,#d2cec8)}
.person-name{font-family:"Arvo",Georgia,serif;font-size:9px;color:var(--rust);margin-top:11px}
.person-loc{font-size:8px;font-style:italic;color:var(--muted);margin-top:3px}

/* green */
.green-title{left:54px;top:980px;font-size:14.5px;color:var(--olive)}
.green-copy{left:54px;top:1005px;width:450px;font-size:8.4px;line-height:16px;color:var(--ink)}
.badge-round{left:543px;top:983px;width:67px;height:63px;border-radius:50%;background:linear-gradient(#3c9a6a,#1e5f8a)}
.badge-blue{left:650px;top:984px;width:59px;height:64px;border-radius:4px;background:linear-gradient(#3a76c4,#1d4c94)}
.badge-cert{left:738px;top:985px;width:64px;height:62px;border:1px solid #ccc;background:linear-gradient(#ffffff 0 66%,#4b79b5 66%)}

/* footer */
.site-footer{left:0;top:1093px;width:864px;height:107px;background:var(--footer)}
.foot-nav{position:absolute;left:56px;top:32px;display:flex;font-size:8px;color:#ddd}
.foot-nav span.sep{margin:0 12px;color:#aaa}
.social{position:absolute;top:25px;left:694px;display:flex;gap:4px}
.social span{width:20px;height:20px;border-radius:50%;background:var(--white)}
.foot-rule{position:absolute;left:54px;top:66px;width:756px;height:1px;background:#3e3c3d}
.copyright{position:absolute;top:82px;width:864px;text-align:center;font-size:8.4px;color:#ddd}
</style>
</head>
<body>

<header class="abs site-header">
  <div class="abs brand"><span class="brand-dot"></span><span class="brand-name">Bright Core Flow</span></div>
  <div class="abs search">
    <svg width="9" height="9" viewBox="0 0 10 10"><circle cx="4" cy="4" r="3" fill="none" stroke="#333" stroke-width="1.6"/><line x1="6.3" y1="6.3" x2="9.2" y2="9.2" stroke="#333" stroke-width="1.8"/></svg>
  </div>
  <nav class="abs main-nav">
    <a class="active" href="#">HOME</a><a href="#">SCHEDULE</a><a href="#">INSTRUCTORS</a><a href="#">RATES</a><a href="#">CONTACT US</a>
  </nav>
</header>

<section class="abs hero">
  <div class="hero-photo" role="img" aria-label="Woman in workout clothes stretching her leg against a pillar under an urban overpass"></div>
  <div class="abs arrow" style="left:28px"><svg width="14" height="16" viewBox="0 0 14 16"><polyline points="10,2 4,8 10,14" fill="none" stroke="#fff" stroke-width="2"/></svg></div>
  <div class="abs arrow" style="left:793px"><svg width="14" height="16" viewBox="0 0 14 16"><polyline points="4,2 10,8 4,14" fill="none" stroke="#fff" stroke-width="2"/></svg></div>
  <h1 class="abs slab hero-title" style="font-weight:400">Emotional &amp; Physical Health</h1>
  <p class="abs hero-copy">Neque porro quisquam est qui dolorem ipsum quia dolor sit amet, consectetur, adipisci velit Neque porro quisquam est qui dolorem ipsum quia dolor sit amet, consectetur, adipisci velit. Neque porro quis.</p>
  <a class="abs btn hero-btn" href="#">Learn More</a>
</section>

<h2 class="abs slab welcome-title" style="font-weight:400">WELCOME</h2>
<div class="abs welcome-avatar" role="img" aria-label="Portrait of the studio instructor stretching"></div>
<h3 class="abs slab welcome-sub" style="font-weight:400">Bright Core Flow Pilates and SpiralMotion® Studio..</h3>
<div class="abs welcome-copy">
  <p>In the heart of Cedar Hollow Village, is a warm, inviting studio where students and teachers alike are supported and encouraged to discover and grow at an individual pace through the field of integrated movement. We offer one-on-one sessions, group reformer classes and mat classes.</p>
  <p>Our mission is to promote long-term emotional and physical health through joyful, integrated movement training and to inspire and nurture our clients to learn more deeply about themselves and connect with fellow students and the community.</p>
</div>
<a class="abs btn welcome-btn" href="#">Learn More</a>
<div class="abs door-photo" role="img" aria-label="Red front door of the studio with a small tree beside the entrance"></div>

<section class="abs testimonials">
  <h2 class="slab">TESTIMONIALS</h2>
  <div class="abs quote-card" style="left:68px">
    <span class="quote-mark"><svg width="13" height="11" viewBox="0 0 13 11"><path d="M0 11V6Q0 1 5 0v2Q2 3 2.5 5H5v6zM7 11V6q0-5 5-6v2q-3 1-2.5 3H12v6z" fill="#fff"/></svg></span>
    <p class="quote-text">Neque porro quisquam est qui dolorem ipsum quia dolor sit amet, consectetur, adipisci velit, Neque porro quisquam est qui dolorem ipsum quia dolor sit amet, consectetur, adipisci velit</p>
  </div>
  <div class="abs person" style="left:83px">
    <div class="person-avatar" role="img" aria-label="Customer portrait"></div>
    <div><div class="person-name">OWEN HALE</div><div class="person-loc">by USA</div></div>
  </div>
  <div class="abs quote-card" style="left:448px">
    <span class="quote-mark"><svg width="13" height="11" viewBox="0 0 13 11"><path d="M0 11V6Q0 1 5 0v2Q2 3 2.5 5H5v6zM7 11V6q0-5 5-6v2q-3 1-2.5 3H12v6z" fill="#fff"/></svg></span>
    <p class="quote-text">Neque porro quisquam est qui dolorem ipsum quia dolor sit amet, consectetur, adipisci velit, Neque porro quisquam est qui dolorem ipsum quia dolor sit amet, consectetur, adipisci velit</p>
  </div>
  <div class="abs person" style="left:463px">
    <div class="person-avatar" role="img" aria-label="Customer portrait"></div>
    <div><div class="person-name">MARA QUINN</div><div class="person-loc">by USA</div></div>
  </div>
</section>

<h2 class="abs slab green-title" style="font-weight:400">We’re Green Certified!</h2>
<p class="abs green-copy">Join our community in creating a sustainable future. We enjoy the benefits of protecting our environment with daily practice: recycling, using efficient lighting, conserving water use, and acting responsibly.</p>
<div class="abs badge-round" role="img" aria-label="Green business program badge"></div>
<div class="abs badge-blue" role="img" aria-label="Local best-of award badge"></div>
<div class="abs badge-cert" role="img" aria-label="Pilates certification badge"></div>

<footer class="abs site-footer">
  <nav class="foot-nav"><span>HOME</span><span class="sep">|</span><span>SCHEDULE</span><span class="sep">|</span><span>INSTRUCTORS</span><span class="sep">|</span><span>RATES</span><span class="sep">|</span><span>CONTACT US</span></nav>
  <div class="social" aria-label="Social links"><span></span><span></span><span></span><span></span><span></span></div>
  <div class="foot-rule"></div>
  <p class="copyright">Copyright (c)2015, Yoursite, All Right Reserved.</p>
</footer>

</body>
</html>
```